I want a website to be designed for our new company, it's an import and export company for variety of things.

please see the attached Logo for our company and the Images for our different sections for our busienss

Target Market(s)

multiple

Coding

Coded - Design and coding required

Number of Pages Required

5+ page

Font styles to use
Sans Serif

Colors

Designer to choose colors to be used in the design.

Requirements
Must have
• KDR WORLDWIDE
• KDR worlwide Supply & Building provides various services. The Company offers infrastructure construction, oil, enegy and gas services, agricultural projects, real estate development, travel and tourism, and food processing and trading.
• Civil contracting for infrastructure, residential and heavy projects. Through its main subsidiaries; distribution of general food products, construction chemicals including corrosion inhibitors and electrical machinery; provides catering and travel agency services; ownership and operation of a school; offers human sources services including manpower supply.
• Drilling and Gold Mines Used Machinery, All Kinds of Construction Machinery, Drilling Machines are manufactured and sold.
Nice to have
• good designa and beautiful colours, it has too look professional

```html
<!DOCTYPE html>
<html lang="en">
<head>
<meta charset="utf-8">
<title>KDR WORLDWIDE – Import and Export Company</title>
<link rel="stylesheet" href="https://fonts.googleapis.com/css2?family=Outfit:wght@300;400;500;600;700&display=swap">
<style>
:root{
  --ink:#1b1b1b;
  --dark:#161616;
  --accent:#f5b300;
  --white:#ffffff;
  --muted:#4a4a4a;
  --line:#cfcfcf;
  --grey-edge:#8a8a8a;
}
*{box-sizing:border-box;margin:0;padding:0}
html,body{width:1200px;height:4138px;overflow:hidden}
body{position:relative;background:var(--white);font-family:'Outfit',sans-serif;color:var(--ink)}
.abs{position:absolute}
a{color:inherit;text-decoration:none}

/* header */
.site-header{left:0;top:0;width:1200px;height:106px;background:var(--dark);z-index:3}
.nav-link{top:40px;color:var(--white);font-size:13px;font-weight:500}
.brand{left:500px;top:30px;width:200px;text-align:center;color:var(--white);font-size:17px;font-weight:600;letter-spacing:2px;display:flex;align-items:center;justify-content:center;gap:8px;height:44px}
.brand-dot{width:10px;height:10px;border-radius:50%;background:var(--accent)}
.social-top{top:38px;width:28px;height:28px;border-radius:50%;background:var(--white)}

/* hero */
.hero{left:0;top:106px;width:1200px;height:601px}
.hero-kicker{left:0;top:292px;width:1200px;text-align:center;color:var(--white);font-size:38px;font-weight:300}
.hero-title{left:0;top:340px;width:1200px;text-align:center;color:var(--white);font-size:74px;font-weight:600}
.scroll-mouse{left:588px;top:610px;width:24px;height:38px;border:2px solid var(--white);border-radius:12px}
.scroll-mouse::after{content:"";position:absolute;left:9px;top:7px;width:2px;height:8px;background:var(--white);border-radius:1px}

/* section titles */
.section-title{left:0;width:1200px;text-align:center;font-size:50px;font-weight:600;color:var(--ink)}
.section-intro{left:200px;top:806px;width:800px;text-align:center;font-size:15.5px;line-height:21px;color:var(--ink)}

/* services */
.service-card{width:317px;height:233px;overflow:hidden}
.service-photo{position:absolute;inset:0}
.service-caption{position:absolute;left:0;bottom:0;width:100%;height:50px;background:rgba(0,0,0,.6);color:var(--white);font-size:16px;display:flex;align-items:center;padding:0 18px;justify-content:space-between}
.arrow-ring{width:28px;height:28px;border:2px solid var(--accent);border-radius:50%;display:flex;align-items:center;justify-content:center}
.btn{background:var(--accent);color:var(--ink);font-weight:600;font-size:15px;display:flex;align-items:center;justify-content:center}

/* about */
.about-title{left:93px;top:1895px;font-size:50px;font-weight:600;color:var(--white)}
.about-text{left:93px;top:1962px;width:480px;font-size:13px;line-height:19px;color:#d9d9d9;font-family:Arial,sans-serif}

/* news */
.news-card{top:2518px;width:331px;height:429px;border:1px solid var(--line);background:var(--white)}
.news-photo{position:absolute;left:0;top:0;width:100%;height:231px}
.news-date{position:absolute;left:70px;top:204px;width:190px;height:44px;background:var(--accent);font-size:15px;font-weight:500;display:flex;align-items:center;justify-content:center;gap:6px}
.news-title{position:absolute;left:0;top:258px;width:100%;text-align:center;font-size:22px;font-weight:500}
.news-text{position:absolute;left:30px;top:300px;width:270px;text-align:center;font-size:12.5px;line-height:18px;color:var(--muted);font-family:Arial,sans-serif}
.news-more{position:absolute;left:0;top:384px;width:100%;text-align:center;font-size:12px;font-weight:600;color:var(--accent)}
.slider-arrow{top:2650px;width:40px;height:96px;background:var(--dark);display:flex;align-items:center;justify-content:center}

/* gallery */
.gallery-tile{}

/* footer */
.footer-brand{left:450px;top:3700px;width:300px;text-align:center;color:var(--white);font-size:22px;font-weight:600;letter-spacing:3px;display:flex;align-items:center;justify-content:center;gap:10px}
.newsletter-title{left:0;top:3808px;width:1200px;text-align:center;color:var(--white);font-size:34px;font-weight:400}
.newsletter-input{left:302px;top:3869px;width:466px;height:42px;background:var(--white);font-size:13px;color:#555;display:flex;align-items:center;padding-left:12px;gap:6px}
.newsletter-btn{left:768px;top:3869px;width:128px;height:42px}
.follow-title{left:0;top:3932px;width:1200px;text-align:center;color:var(--white);font-size:28px}
.social-foot{top:3980px;width:38px;height:38px;border-radius:50%}
.footer-rule{left:0;top:4068px;width:1200px;height:1px;background:#3a3a3a}
.copyright{left:0;top:4096px;width:1200px;text-align:center;font-size:12px;color:#8a8a8a}
.copyright span{color:var(--accent)}
</style>
</head>
<body>

<header class="abs site-header">
  <a class="abs nav-link" style="left:245px">Home</a>
  <a class="abs nav-link" style="left:325px">About us</a>
  <a class="abs nav-link" style="left:423px">Services</a>
  <div class="abs brand"><span class="brand-dot"></span>KDR WORLDWIDE</div>
  <a class="abs nav-link" style="left:726px">Gallery</a>
  <a class="abs nav-link" style="left:814px">News</a>
  <a class="abs nav-link" style="left:890px">Contact Us</a>
  <span class="abs social-top" style="left:1003px" aria-label="Social link"></span>
  <span class="abs social-top" style="left:1039px" aria-label="Social link"></span>
  <span class="abs social-top" style="left:1076px" aria-label="Social link"></span>
</header>

<svg class="abs hero" viewBox="0 0 1200 601" role="img" aria-label="Yellow mining trucks and loader on a rocky quarry road">
  <defs>
    <linearGradient id="heroSky" x1="0" y1="0" x2="1" y2="1">
      <stop offset="0" stop-color="#9aa0a8"/>
      <stop offset=".55" stop-color="#7c7a72"/>
      <stop offset="1" stop-color="#5d4a30"/>
    </linearGradient>
    <linearGradient id="heroRock" x1="0" y1="0" x2="0" y2="1">
      <stop offset="0" stop-color="#b07a2e" stop-opacity=".0"/>
      <stop offset="1" stop-color="#4b3b26" stop-opacity=".7"/>
    </linearGradient>
  </defs>
  <path d="M0 0H1200V530C1020 535 900 560 800 585C690 612 520 612 410 585C310 562 180 535 0 530Z" fill="url(#heroSky)"/>
  <path d="M0 0H1200V530C1020 535 900 560 800 585C690 612 520 612 410 585C310 562 180 535 0 530Z" fill="url(#heroRock)"/>
</svg>
<div class="abs hero-kicker">Import and Export Company</div>
<div class="abs hero-title">For Variety Of Things</div>
<div class="abs scroll-mouse"></div>
<svg class="abs" style="left:592px;top:652px" width="16" height="14" viewBox="0 0 16 14"><path d="M3 2l5 5 5-5M3 7l5 5 5-5" fill="none" stroke="#fff" stroke-width="1.5"/></svg>

<h2 class="abs section-title" style="top:738px">Our Services</h2>
<p class="abs section-intro">Lorem ipsum dolor sit amet, consectetur adipiscing elit. Curabitur pretium, erat in mattis fringilla,<br>lacus urna porta lectus, et vestibulum arcu nibh sit amet nibh.</p>

<!-- services grid -->
<div class="abs service-card" style="left:93px;top:875px">
  <div class="service-photo" role="img" aria-label="Engineers in hard hats reviewing plans at a building site" style="background:linear-gradient(160deg,#d8d8d6,#9c9c98 60%,#c06a2a)"></div>
  <div class="service-caption">Construction<span class="arrow-ring"><svg width="10" height="12" viewBox="0 0 10 12"><path d="M3 1l5 5-5 5" fill="none" stroke="#f5b300" stroke-width="2"/></svg></span></div>
</div>
<div class="abs service-card" style="left:442px;top:875px">
  <div class="service-photo" role="img" aria-label="Oil refinery towers at sunset" style="background:linear-gradient(170deg,#c26a3a,#7a4a3a 50%,#3a2c2c)"></div>
  <div class="service-caption">Oil, Enegy and Gas Service<span class="arrow-ring"><svg width="10" height="12" viewBox="0 0 10 12"><path d="M3 1l5 5-5 5" fill="none" stroke="#f5b300" stroke-width="2"/></svg></span></div>
</div>
<div class="abs service-card" style="left:789px;top:875px">
  <div class="service-photo" role="img" aria-label="Green crop rows on farmland with hills" style="background:linear-gradient(180deg,#cfe0ef,#7fa35a 35%,#3d6e22)"></div>
  <div class="service-caption">Agricultural Projects<span class="arrow-ring"><svg width="10" height="12" viewBox="0 0 10 12"><path d="M3 1l5 5-5 5" fill="none" stroke="#f5b300" stroke-width="2"/></svg></span></div>
</div>
<div class="abs service-card" style="left:93px;top:1132px">
  <div class="service-photo" role="img" aria-label="Tower crane above a building under construction at dusk" style="background:linear-gradient(180deg,#1e4f9a,#5a7fb8 40%,#e2a540 75%,#6a4a2a)"></div>
  <div class="service-caption">Real Estate Development<span class="arrow-ring"><svg width="10" height="12" viewBox="0 0 10 12"><path d="M3 1l5 5-5 5" fill="none" stroke="#f5b300" stroke-width="2"/></svg></span></div>
</div>
<div class="abs service-card" style="left:442px;top:1132px">
  <div class="service-photo" role="img" aria-label="Travel items: hat, toy plane, camera and passport" style="background:linear-gradient(160deg,#4a4a4a,#2e2e2e 60%,#3a3a3a)"></div>
  <div class="service-caption">Travel and Tourism<span class="arrow-ring"><svg width="10" height="12" viewBox="0 0 10 12"><path d="M3 1l5 5-5 5" fill="none" stroke="#f5b300" stroke-width="2"/></svg></span></div>
</div>
<div class="abs service-card" style="left:789px;top:1132px">
  <div class="service-photo" role="img" aria-label="Business handshake over a desk" style="background:linear-gradient(160deg,#b88a5a,#e6cfb0 50%,#9a9a9a)"></div>
  <div class="service-caption">Processing and Trading<span class="arrow-ring"><svg width="10" height="12" viewBox="0 0 10 12"><path d="M3 1l5 5-5 5" fill="none" stroke="#f5b300" stroke-width="2"/></svg></span></div>
</div>
<div class="abs service-card" style="left:93px;top:1389px">
  <div class="service-photo" role="img" aria-label="Workers pouring concrete from a chute" style="background:linear-gradient(160deg,#5a5a58,#a9a8a2 50%,#4a5a3a)"></div>
  <div class="service-caption">Civil Contracting<span class="arrow-ring"><svg width="10" height="12" viewBox="0 0 10 12"><path d="M3 1l5 5-5 5" fill="none" stroke="#f5b300" stroke-width="2"/></svg></span></div>
</div>
<div class="abs service-card" style="left:442px;top:1389px">
  <div class="service-photo" role="img" aria-label="Two engineers in safety vests among high-rise buildings" style="background:linear-gradient(170deg,#8a98a8,#5a6270 50%,#c46a2a)"></div>
  <div class="service-caption">Residential and Heavy Projects<span class="arrow-ring"><svg width="10" height="12" viewBox="0 0 10 12"><path d="M3 1l5 5-5 5" fill="none" stroke="#f5b300" stroke-width="2"/></svg></span></div>
</div>
<div class="abs service-card" style="left:789px;top:1389px">
  <div class="service-photo" role="img" aria-label="Lit underground mine tunnel" style="background:radial-gradient(circle at 55% 55%,#e8c070,#8a5a2a 35%,#2e1e12)"></div>
  <div class="service-caption">Drilling and Gold Mines<span class="arrow-ring"><svg width="10" height="12" viewBox="0 0 10 12"><path d="M3 1l5 5-5 5" fill="none" stroke="#f5b300" stroke-width="2"/></svg></span></div>
</div>

<a class="abs btn" style="left:511px;top:1646px;width:178px;height:48px">View All Services</a>

<!-- about -->
<svg class="abs" style="left:0;top:1740px" width="1200" height="665" viewBox="0 0 1200 665">
  <path d="M0 88C200 82 330 72 430 45C530 15 670 10 770 40C870 70 1000 82 1200 88V580C1000 588 870 600 770 630C670 660 530 660 430 630C330 600 200 588 0 580Z" fill="var(--grey-edge)"/>
  <path d="M0 94C200 88 330 78 430 52C530 22 670 18 770 48C870 77 1000 88 1200 94V578C1000 584 870 596 770 624C670 652 530 652 430 624C330 596 200 584 0 578Z" fill="var(--dark)"/>
</svg>
<h2 class="abs about-title">About Us</h2>
<p class="abs about-text">Lorem ipsum dolor sit amet, consectetur adipiscing elit. Curabitur pretium, erat in mattis fringilla, lacus porta lectus, et vestibulum arcu nibh sit amet nibh. Nunc at nisl libero. Nullam eu magna faucibus, faucibus ligula ac, convallis tellus. Morbi a nunc et orci suscipit cursus porta eget leo.&nbsp; Nunc non metus arcu. Praesent a lacus vitae urna malesuada ullamcorper vel quis ligula. Nunc facilisis vestibulum nibh, ut vehicula mi iaculis vitae.</p>
<a class="abs btn" style="left:93px;top:2120px;width:141px;height:48px">Read More</a>
<svg class="abs" style="left:615px;top:1820px" width="460" height="465" viewBox="0 0 460 465">
  <defs>
    <linearGradient id="aboutPhoto" x1="0" y1="0" x2="1" y2="1">
      <stop offset="0" stop-color="#f2f3f5"/>
      <stop offset=".55" stop-color="#b8c4d0"/>
      <stop offset="1" stop-color="#e06a7a"/>
    </linearGradient>
  </defs>
  <path d="M150 40C200 10 260 10 310 40L400 95C440 120 455 160 450 210L445 300C440 350 410 390 360 415L270 455C230 470 190 465 150 445L60 395C20 370 0 330 5 280L10 190C15 140 40 105 80 85Z" fill="var(--accent)"/>
  <path d="M170 30C215 5 265 5 305 30L390 85C425 110 440 150 435 195L430 305C425 350 395 385 350 405L265 445C225 460 190 458 155 440L70 385C35 360 20 320 25 280L30 180C35 135 60 100 100 80Z" fill="url(#aboutPhoto)" role="img" aria-label="Engineer in a hard hat blended with a city skyline"/>
</svg>

<!-- news -->
<h2 class="abs section-title" style="top:2457px">Latest News</h2>

<article class="abs news-card" style="left:95px">
  <div class="news-photo" role="img" aria-label="Industrial plant lit up at twilight" style="background:linear-gradient(180deg,#6a6a9a,#b07a8a 35%,#3a3a40 70%,#d0a040)"></div>
  <div class="news-date"><svg width="16" height="15" viewBox="0 0 16 15"><rect x="1" y="2" width="14" height="12" fill="none" stroke="#1b1b1b" stroke-width="1.5"/><path d="M1 6h14M5 0v4M11 0v4" stroke="#1b1b1b" stroke-width="1.5"/></svg>02 January, 2020</div>
  <h3 class="news-title">Duis sit amet nulla</h3>
  <p class="news-text">Duis vel ultrices nibh, ut tincidunt quam. Donec aliquam vitae lacus a finibus. Nullam malesuada vitae libero eu interdum. Vivamus diam nunc, sodales</p>
  <a class="news-more">Read More</a>
</article>
<article class="abs news-card" style="left:435px">
  <div class="news-photo" role="img" aria-label="Hands holding a tablet inside a greenhouse of seedlings" style="background:linear-gradient(180deg,#e4e8ea,#b8c8b0 45%,#5e9a3a)"></div>
  <div class="news-date"><svg width="16" height="15" viewBox="0 0 16 15"><rect x="1" y="2" width="14" height="12" fill="none" stroke="#1b1b1b" stroke-width="1.5"/><path d="M1 6h14M5 0v4M11 0v4" stroke="#1b1b1b" stroke-width="1.5"/></svg>02 January, 2020</div>
  <h3 class="news-title">Duis sit amet nulla</h3>
  <p class="news-text">Duis vel ultrices nibh, ut tincidunt quam. Donec aliquam vitae lacus a finibus. Nullam malesuada vitae libero eu interdum. Vivamus diam nunc, sodales</p>
  <a class="news-more">Read More</a>
</article>
<article class="abs news-card" style="left:776px">
  <div class="news-photo" role="img" aria-label="Yellow dump trucks on a coal mining site" style="background:linear-gradient(180deg,#5a5a5a,#8a8a86 40%,#c9a030 60%,#3a3a3a)"></div>
  <div class="news-date"><svg width="16" height="15" viewBox="0 0 16 15"><rect x="1" y="2" width="14" height="12" fill="none" stroke="#1b1b1b" stroke-width="1.5"/><path d="M1 6h14M5 0v4M11 0v4" stroke="#1b1b1b" stroke-width="1.5"/></svg>02 January, 2020</div>
  <h3 class="news-title">Duis sit amet nulla</h3>
  <p class="news-text">Duis vel ultrices nibh, ut tincidunt quam. Donec aliquam vitae lacus a finibus. Nullam malesuada vitae libero eu interdum. Vivamus diam nunc, sodales</p>
  <a class="news-more">Read More</a>
</article>
<a class="abs slider-arrow" style="left:76px" aria-label="Previous"><svg width="14" height="24" viewBox="0 0 14 24"><path d="M12 2L2 12l10 10" fill="none" stroke="#fff" stroke-width="2.5"/></svg></a>
<a class="abs slider-arrow" style="left:1086px" aria-label="Next"><svg width="14" height="24" viewBox="0 0 14 24"><path d="M2 2l10 10-10 10" fill="none" stroke="#fff" stroke-width="2.5"/></svg></a>

<!-- gallery -->
<div class="abs gallery-tile" style="left:93px;top:3006px;width:458px;height:257px;background:linear-gradient(180deg,#c9a070,#e0b060 55%,#5a4630)" role="img" aria-label="Engineers at sunset near a construction crane"></div>
<div class="abs gallery-tile" style="left:557px;top:3006px;width:273px;height:257px;background:linear-gradient(160deg,#2a2420,#8a6a50 50%,#3a2e26)" role="img" aria-label="Miner holding a gold nugget"></div>
<div class="abs gallery-tile" style="left:837px;top:3006px;width:273px;height:257px;background:linear-gradient(180deg,#4a8ad0,#a8c8e0 50%,#6a5a40)" role="img" aria-label="Excavator loading earth under a blue sky"></div>
<div class="abs gallery-tile" style="left:93px;top:3271px;width:273px;height:257px;background:linear-gradient(160deg,#e8e8e8,#9a9a9e 50%,#4a4a4e)" role="img" aria-label="Stainless steel processing machinery"></div>
<div class="abs gallery-tile" style="left:373px;top:3271px;width:271px;height:257px;background:linear-gradient(180deg,#e8e0d0,#7aa04a 50%,#6a4a30)" role="img" aria-label="Young corn plants in tilled soil"></div>
<div class="abs gallery-tile" style="left:650px;top:3271px;width:460px;height:257px;background:linear-gradient(160deg,#c8b090,#e8dcc8 50%,#8a6a4a)" role="img" aria-label="Tourists in hats exploring an old town"></div>

<a class="abs btn" style="left:517px;top:3544px;width:166px;height:49px">View All</a>

<!-- footer -->
<svg class="abs" style="left:0;top:3622px" width="1200" height="516" viewBox="0 0 1200 516">
  <path d="M0 88C180 86 300 76 400 44C500 12 700 12 800 44C900 76 1020 86 1200 88V516H0Z" fill="var(--grey-edge)"/>
  <path d="M0 96C180 94 300 84 400 52C500 22 700 22 800 52C900 84 1020 94 1200 96V516H0Z" fill="var(--dark)"/>
</svg>
<div class="abs footer-brand"><span class="brand-dot" style="width:14px;height:14px"></span>KDR WORLDWIDE</div>
<h2 class="abs newsletter-title">Newsletter Subscribe</h2>
<div class="abs newsletter-input"><svg width="14" height="10" viewBox="0 0 14 10"><rect x=".5" y=".5" width="13" height="9" fill="none" stroke="#777"/><path d="M.5 .5l6.5 5 6.5-5" fill="none" stroke="#777"/></svg>Enter email address</div>
<a class="abs btn newsletter-btn">Subscribe</a>
<h3 class="abs follow-title">Follow us</h3>
<span class="abs social-foot" style="left:532px;background:var(--accent)" aria-label="Social link"></span>
<span class="abs social-foot" style="left:580px;background:#555" aria-label="Social link"></span>
<span class="abs social-foot" style="left:627px;background:#555" aria-label="Social link"></span>
<div class="abs footer-rule"></div>
<p class="abs copyright">© 2020 <span>KDR WORLDWIDE</span>. All Rights Reserved.</p>

</body>
</html>
```